Personal coach needs design for inspirational essay 4-page brochure

Overview:
This is a brochure, 11”x17” that folds to 8-1/2”x11” with 4 pages. Think of it as an oversize greeting card. It may be easiest to understand if you print out the copy and follow it along with descriptions below.
• Front cover: photograph of my embroidery sampler (jpeg photo attached)
• Inside spread: Copy with appropriate graphic elements that depict embroidery
• Back cover: contact information, brief descriptive copy, a thumbnail photo of original antique sampler (jpeg photo attached)
Copy for front cover title, inside spread and back cover is attached
Purpose of brochure:
Once a year, I produce a 4-page illustrated philosophical essay, which invites personal reflection on living a more mindful, meaningful life. I have this printed as hard copy. I have attached a few examples from previous years (Every Morning Brings Rain (Sketch Harbor created this for me last year), Lanterns, Letters from Willows). Each has a unique design related to its theme.
Concept:
This year’s essay theme, “I am a child of light. I walk in love and live in beauty” is based on a quote that I included in an embroidery sample that I made, which is a replica of an antique sampler. All this ls described in the copy I wrote for the inside spread.
Design Guidance:
Front cover: I want to use a photo of my actual sampler. I am not sure how big you can make it, given the resolution of the photo which I took from my Zelvo. So, the cover would include this photo plus the words “I am a child of light. I walk in love and live in beauty.” Given the colors of my embroidery, I imagine a color palette of pastel pink, green or blue – to go along with the sampler. But I am also open to suggestions.
Inside Spread: Along with the copy, I envision incorporating some graphic elements that depict the art of embroidery, e.g.: scissors, a spool of thread, a threaded needle, etc. At the end of my document with copy is a page describing some potential graphic elements to explore, along with a couple examples of line drawings of those kind of objects.
Back cover: If you look at some of the other examples I’ve sent, you’ll see how this cover is typically handled. Place a reduced thumbnail version of the actual brochure cover near the line that says this is the 17th in a series. Then, there’s a jpeg photo of the actual antique sampler that should be placed next to the copy that says “About the original sampler.” If the jpeg isn't good, look at the original on this site: https://archive.fernwoodcollections.org/objects/40512/sampler-by-edith-hallows
A couple of questions have come up for my project, relevant to all designers:
1. Ultimately, I need a print-ready pdf, complete with crop marks. I need to be able to give the printer camera-ready artwork that he can digitally print from.
2. The overall mood I'm looking for in this piece: feminine, soft elegance, subtle, flowing, very soft/pastel (think very, very pale shell pink with perhaps a cream or soft gray as accent). No photography or 4-color art. And to repeat what I said in the project description: NO sewing machines, dress forms, safety pins, irons -- use only line drawings related to embroidery, e.g.: spools of thread, threaded needles, thimble, scissors.
Thank you.

```html
<!DOCTYPE html>
<html lang="en">
<head>
<meta charset="utf-8">
<title>I Am a Child of Light – Essay Brochure</title>
<link href="https://fonts.googleapis.com/css2?family=Arvo:ital,wght@0,400;0,700;1,400&family=Noticia+Text:ital,wght@0,400;0,700;1,400&display=swap" rel="stylesheet">
<style>
:root{
  --backdrop:#5e9ea5;
  --paper:#d9d8d3;
  --ink:#1f1f1c;
  --heading:#3d3d33;
  --quote:#55544c;
  --frame:#9b9a95;
  --frame-inner:#e9e7e1;
  --silver-a:#f3f3f3;
  --silver-b:#b9b9b9;
  --sampler-a:#d8c9a8;
  --sampler-b:#8d8a5a;
  --engrave-a:rgba(150,147,140,.55);
  --engrave-b:rgba(217,216,211,0);
}
*{margin:0;padding:0;box-sizing:border-box}
html,body{width:865px;height:1200px;overflow:hidden}
body{background:var(--backdrop);position:relative;font-family:"Noticia Text",Georgia,serif;color:var(--ink)}
.spread{position:absolute;left:34px;width:797px;height:514px;background:var(--paper);box-shadow:8px 10px 14px rgba(0,0,0,.35)}
.spread--outside{top:60px}
.spread--inside{top:631px}
.abs{position:absolute}

/* back cover */
.series-strip{left:34px;top:30px;width:329px;height:90px;display:flex}
.series-thumb{width:66px;height:90px;background:#e2e0da;border:1px solid #c6c4be;padding:3px;font-family:"Arvo",serif;font-size:3.6px;line-height:4px;color:var(--heading)}
.series-thumb .mini{height:56px;margin:2px 4px;background:linear-gradient(var(--sampler-a),var(--sampler-b));border:2px solid var(--frame)}
.series-note{flex:1;background:linear-gradient(100deg,var(--silver-a) 10%,#d6d6d6 45%,var(--silver-b) 80%,#e6e6e6);padding:18px 6px 0 10px;font-size:9.3px;line-height:12px;position:relative}
.series-note b{font-weight:700}
.series-note .year{position:absolute;right:10px;bottom:14px;font-weight:700;font-size:8px}
.contact{top:143px;left:34px;font-size:8.4px;line-height:11px}
.contact--right{left:236px;top:165px}
.divider{left:0;top:192px;width:460px;height:3px;background:linear-gradient(90deg,transparent,#55544e 20%,#55544e 70%,transparent);border-radius:2px;opacity:.8}
.original-photo{left:34px;top:223px;width:77px;height:111px;border:2px solid #2a2a26;background:linear-gradient(#e0c9a6,#c9ab83 60%,#9a8b5b)}
.section-title{font-family:"Arvo",serif;font-weight:700;font-size:12.5px;line-height:15px;color:var(--heading);text-transform:uppercase}
.about-original{left:119px;top:222px;width:278px}
.about-embroidered{left:34px;top:358px;width:330px}
.section-body{font-size:6.9px;line-height:9.3px;margin-top:4px}

.cover-title{font-family:"Arvo",serif;font-weight:700;font-size:21px;line-height:28px;color:var(--heading);text-transform:uppercase}
.cover-title--top{left:447px;top:16px}
.cover-title--bottom{left:466px;top:442px}
.q{font-size:30px;line-height:1;vertical-align:top}
.sampler-frame{left:466px;top:76px;width:289px;height:362px;background:var(--frame);padding:10px}
.sampler-frame .mat{width:100%;height:100%;background:var(--frame-inner);padding:4px}
.sampler-photo{width:100%;height:100%;background:linear-gradient(#d9cfb4 0%,#d4c6a2 55%,#a59a63 85%,#6f7142 100%)}

/* inside spread */
.engraving{left:300px;top:205px;width:225px;height:290px;border-radius:40% 40% 10% 10%;background:radial-gradient(ellipse at 50% 55%,var(--engrave-a),var(--engrave-b) 70%)}
.essay{font-size:8.7px;line-height:11px}
.essay p{margin-bottom:11px}
.essay--left{left:28px;top:48px;width:330px}
.essay--left .narrow{width:283px}
.essay--left .third{margin-top:18px;width:222px}
.essay--right{left:433px;top:48px;width:345px;text-align:right}
.essay--right .inset{padding-left:95px}
.closing-quote{left:575px;top:428px;width:205px;font-family:"Arvo",serif;font-weight:400;font-size:18px;line-height:24px;color:var(--quote)}
.closing-quote .line{display:block;white-space:nowrap;padding-left:12px}
.closing-quote .mark{font-weight:700;font-size:22px;line-height:18px;vertical-align:top}
.closing-quote .line--first{padding-left:0}
</style>
</head>
<body>

<section class="spread spread--outside">
  <div class="abs series-strip">
    <div class="series-thumb">"I AM<br>A CHILD OF LIGHT<div class="mini" role="img" aria-label="Small cover preview with embroidered sampler"></div>I WALK IN LOVE &amp;<br>LIVE IN BEAUTY"</div>
    <div class="series-note"><b>I am a child of light</b> is the 17th in a series of Labor Day essays inviting a moment of reflection on living a more meaningful, more mindful life<span class="year">©2024</span></div>
  </div>

  <div class="abs contact">Maren Ellsworth Tate, Ph.D.<br>Heron Bank House<br>18 Orchard Lane<br>Westbrook Harbor, Massachusetts&nbsp;&nbsp;01990</div>
  <div class="abs contact contact--right">Mobile:&nbsp; 978-555-0142<br>Email: mtate@harbormail.net</div>
  <div class="abs divider"></div>

  <div class="abs original-photo" role="img" aria-label="Photo of the antique sampler with alphabets, trees and a deer"></div>
  <div class="abs about-original">
    <h2 class="section-title">About the<br>Original Sampler</h2>
    <p class="section-body">The embroidery sampler that I reproduced is a part of the Fernwood Collections textile collection and is known as "The Chase Sampler" because of the dog chasing a leaping stag. It is considered a rare example of American needlework design because it combines an embroidered picture with alphabet lists and includes the embroiderer's name (Edith Hallows), place of birth, date the sampler was made, as well as a pious statement: Goodness and Mercy Ever follow those who shape their Conduct by Gods Holy Laws.</p>
  </div>

  <div class="abs about-embroidered">
    <h2 class="section-title">About Embroidered<br>Samplers</h2>
    <p class="section-body">In Colonial days, needlework skills were important for the future management of a girl's household. Alphabets allowed girls to practice the marking of linen; sheets, undergarments and other personal items were initialed or named so they came back to their right owners after wash day. Various motifs and border patterns were used to decorate both clothes and domestic furnishings. In these times there were no pattern books, so when women saw a stitch they wanted to use, they quickly sewed a small example on a piece of cloth – their "sampler." The completed work was usually framed and hung in the parlor as a testament to the maker's obedience, patience, and skill.</p>
  </div>

  <h1 class="abs cover-title cover-title--top"><span class="q">"</span>I am<br>&nbsp;A child of light</h1>
  <div class="abs sampler-frame"><div class="mat"><div class="sampler-photo" role="img" aria-label="Photo of the hand-stitched sampler with alphabets, flowers, trees and animals"></div></div></div>
  <p class="abs cover-title cover-title--bottom">I walk in love &amp;<br>live in beauty <span class="q">"</span></p>
</section>

<section class="spread spread--inside">
  <div class="abs engraving" role="img" aria-label="Engraving of a colonial woman seated on a chair doing embroidery"></div>

  <div class="abs essay essay--left">
    <p>Nearly fifty years ago as a young bride in the historic seaport of Westbrook Harbor, Massachusetts, I became intrigued by 18th century embroidery samplers, created by young girls as part of their education to learn basic needlework skills needed to operate the family household. Samplers depicting alphabets and numerals served as a pattern book -- from simple cross-stitch, back-stitch and whip-stitch to more elaborate techniques like chain-stitch, blanket-stitch, satin-stitch, and French knots.</p>
    <p class="narrow">As luck had it, I chanced upon a kit to create a replica of a sampler sewn in 1760 by 11-year-old Edith Hallows. My sewing skills were extremely limited (I am a duct tape &amp; staple hemmer), but I was determined to recreate this charming artifact of colonial life in our picturesque harbor town.</p>
    <p class="third">Four needle-pricking, patience-worn, eye-straining years later, my sampler was nearly finished. Despite my clumsy stitches, it was a silk-threaded marvel of rainbow-colored alphabets, urns of flowers and vines, scrolling flourishes and geometric borders, deer and rabbits gamboling under a fruit tree. Edith's original sampler – like many -- featured a pious religious statement, so all my piece lacked was a Bible verse or moral quotation that would personalize my piece for posterity. Given the endless pokes, jabs and mind-numbing tedium I had experienced in the making of my sampler, I was tempted to stitch a record of my frustration: "I vow never to attempt a #%$&amp;!# sampler ever again!" Sobered by the potential shame of how this might reflect on me 100 years hence, I instead recalled an inspirational verse I had often used in meditation: <i>"I am a child of light. I walk in love and live in beauty."</i></p>
  </div>

  <div class="abs essay essay--right">
    <p>More aspirational than representative of my life, those words were like a light at the end of a tunnel -- guiding me toward a way of being that I wanted to be more of my default. Words have a power that we don't often appreciate in ordinary speech, as depicted in many stories about magic spells. There may be a basis of truth at the heart of these fairy tales. For example, the sorcerer's incantation abracadabra is reputed to come from the Hebrew and means "I create what I speak" – or at root, "what is spoken is what becomes." With a wave of a wand and recitation of the word, shazam! --magic can happen!</p>
    <p class="inset">This is more than just woo-woo New Age thinking. There's also science behind how the way we speak and what we say shapes our perceptions, actions and experiences. Positive affirmations can create and strengthen neural pathways in our brain, serving as a kind of unconscious compass to point us in the direction we want to go. For me, the words of my sampler remind me to lean into moments where I feel joy and lightness</p>
    <p class="inset">The dark hours of our being have their place in our lives, and while they can be painful or unwanted, there is even sometimes safety or solace in shadow. In truth, we cannot have one without the other – much like a flower whose petals reach up toward the light must also let its roots dangle deeply in soil. Yet, there are moments like when my beloved grandson Owen reaches up to hug me spontaneously or when a piece of music enthralls me or when the eyes of my barista smile as I put a small tip in her jar, I am indeed "a child of light, walking in love and living in beauty."</p>
  </div>

  <p class="abs closing-quote">
    <span class="line line--first"><span class="mark">"</span>I am a child of light.</span>
    <span class="line">I walk in love and</span>
    <span class="line">live in beauty.<span class="mark">"</span></span>
  </p>
</section>

</body>
</html>
```